Quillmere Business Card

I have a current card that I like it just needs a couple little changes to make it perfect. I would like the font size bigger so it could be easily read by older customers.

Business

```html
<!DOCTYPE html>
<html lang="en">
<head>
<meta charset="utf-8">
<title>Quillmere Business Card</title>
<link href="https://fonts.googleapis.com/css2?family=Arimo:wght@400&family=Source+Sans+3:wght@400&display=swap" rel="stylesheet">
<style>
  :root {
    --page: #ffffff;
    --card: #242424;
    --card-edge: #1b1b1b;
    --green: #5cbb1c;
    --grey: #a9afb0;
    --light: #c9cccd;
    --label: #111111;
  }
  * { box-sizing: border-box; margin: 0; padding: 0; }
  html, body { width: 1060px; height: 1200px; overflow: hidden; background: var(--page); }
  body { position: relative; font-family: "Source Sans 3", sans-serif; }

  .side-label { position: absolute; left: 0; width: 1060px; text-align: center; font-size: 24px; color: var(--label); }
  .side-label.front { top: 6px; }
  .side-label.back { top: 1148px; }

  .card {
    position: absolute; left: 62px; width: 936px; height: 535px;
    background: radial-gradient(ellipse at 50% 45%, #2c2c2c 0%, var(--card) 55%, var(--card-edge) 100%);
    overflow: hidden;
  }
  .card.front { top: 40px; }
  .card.back { top: 605px; }

  .wordmark { position: absolute; left: 0; width: 936px; text-align: center; }
  .wordmark .name { font-family: "Arimo", sans-serif; font-size: 56px; line-height: 1; color: var(--green); letter-spacing: 1px; }
  .wordmark .sub { font-family: "Arimo", sans-serif; font-size: 20px; color: var(--grey); letter-spacing: 5.5px; margin-top: 4px; }
  .front .wordmark { top: 30px; }
  .back .wordmark { top: 206px; }

  .tagline { position: absolute; top: 106px; left: 0; width: 936px; text-align: center; font-size: 24px; color: var(--green); }

  .brand-mark { position: absolute; display: flex; align-items: center; gap: 14px; }
  .brand-mark .dot { border-radius: 50%; background: var(--grey); flex: none; }
  .brand-mark .mark-name { color: var(--grey); }
  .front .brand-mark { left: 48px; top: 250px; }
  .front .brand-mark .dot { width: 90px; height: 90px; }
  .front .brand-mark .mark-name { font-size: 44px; }
  .back .brand-mark { left: 382px; top: 90px; gap: 10px; }
  .back .brand-mark .dot { width: 46px; height: 46px; }
  .back .brand-mark .mark-name { font-size: 26px; }

  .contact { position: absolute; left: 515px; top: 164px; font-size: 23px; line-height: 1.35; color: var(--light); }
  .contact .address { margin-bottom: 6px; }
  .contact .person { font-size: 28px; color: var(--green); margin-bottom: 6px; }
  .contact .web { margin-bottom: 12px; }

  .hours { position: absolute; left: 0; width: 936px; top: 493px; text-align: center; font-size: 21px; color: var(--light); white-space: nowrap; }

  .seasons { position: absolute; left: 0; width: 936px; top: 448px; display: flex; justify-content: center; gap: 14px; }
  .seasons svg { width: 30px; height: 30px; }
  .seasons-line { position: absolute; left: 0; width: 936px; top: 482px; text-align: center; font-size: 21px; color: var(--light); }
</style>
</head>
<body>
  <div class="side-label front">Front</div>

  <section class="card front">
    <div class="wordmark">
      <div class="name">QUILLMERE</div>
      <div class="sub">Motorsports and Marine</div>
    </div>
    <p class="tagline">Servicing all makes and models of boats, snowmobiles, motorcycles and ATV’s.</p>

    <div class="brand-mark">
      <span class="dot"></span>
      <span class="mark-name">Quillmere</span>
    </div>

    <div class="contact">
      <p class="address">4820 128th Street West<br>Lakeview, MN 55090</p>
      <p class="person">Dale Harmon</p>
      <p>dale@quillmeremotorsports.com</p>
      <p class="web">www.quillmeremotorsports.com</p>
      <p>651.555.0142 Phone<br>651.555.0187 Fax</p>
    </div>

    <p class="hours">Hours: Mon - Wed 9am - 5:30pm • Thurs 9am - 7pm • Fri 9am - 5:30pm • Sat 9am - 3:30pm</p>
  </section>

  <section class="card back">
    <div class="brand-mark">
      <span class="dot"></span>
      <span class="mark-name">Quillmere</span>
    </div>
    <div class="wordmark">
      <div class="name">QUILLMERE</div>
      <div class="sub">Motorsports and Marine</div>
    </div>

    <div class="seasons">
      <svg viewBox="0 0 30 30" aria-label="Water drop"><path d="M15 3 C19 10 23 14 23 19 A8 8 0 0 1 7 19 C7 14 11 10 15 3 Z" fill="#8a9092"/></svg>
      <svg viewBox="0 0 30 30" aria-label="Sun"><circle cx="15" cy="15" r="7" fill="#6e7273"/><g stroke="#6e7273" stroke-width="2.5"><line x1="15" y1="2" x2="15" y2="7"/><line x1="15" y1="23" x2="15" y2="28"/><line x1="2" y1="15" x2="7" y2="15"/><line x1="23" y1="15" x2="28" y2="15"/><line x1="6" y1="6" x2="9" y2="9"/><line x1="21" y1="21" x2="24" y2="24"/><line x1="24" y1="6" x2="21" y2="9"/><line x1="6" y1="24" x2="9" y2="21"/></g></svg>
      <svg viewBox="0 0 30 30" aria-label="Leaf"><path d="M15 3 C24 8 26 18 15 25 C4 18 6 8 15 3 Z" fill="#8a9092"/><line x1="15" y1="8" x2="15" y2="29" stroke="#242424" stroke-width="1.5"/></svg>
      <svg viewBox="0 0 30 30" aria-label="Snowflake"><g stroke="#a9afb0" stroke-width="2" stroke-linecap="round"><line x1="15" y1="3" x2="15" y2="27"/><line x1="4.6" y1="9" x2="25.4" y2="21"/><line x1="4.6" y1="21" x2="25.4" y2="9"/></g></svg>
    </div>
    <p class="seasons-line">Fun for all seasons!</p>
  </section>

  <div class="side-label back">Back</div>
</body>
</html>
```